Retail Appliance Store Chain needs NEW business Card

Name of my company is Brennan's Appliances brennansappliances.example is our website. . We are a 2 location brick and mortar, and online store selling premium, luxury, and normal household appliances, such as ovens, stoves, cooktops, dishwashers, refrigerators, washers and dryers, grills, air conditioners etc. The focus is on large kitchen appliances and laundry appliances.
Please visit http://brennansappliances.example to get a feel for the business and branding.
I have attached the Brennan's Appliances logo (i do not have eps or psd or ai). And I have also attached our current business cards that we use. We have two versions. A double sided version for managers, and a one side version for regular employees.
Please submit BOTH one sided and two sided designs if possible.
Please keep consistent with the Brennan's Appliances logo, colors, etc.
I would prefer no rounded corners on the business card designs for printing costs.
Information on the cards (in no particular order):
Name - Employee Name
Business name - Brennan's Appliances
website - brennansappliances.example
Email - Employee Email
2 Phone Numbers - store 1 address, store 2 address
2 Addresses - store 1 address, store 2 address

*do NOT need Fax #

Industry/Entity Type

Home Appliance

Contact Information for Business Card

Logo - Brennans Appliances Logo
Name - Employee Name
Email - Employee Email

Please no rounded corners. Standard US Business Card Size please.

Font styles to use
Serif
Sans Serif

Requirements
Must have
• colors and design that somewhat match the feel of current logo and website
Should not have
• No rounded corners.
No non-traditional business card size. US Standard Business Card Size only

```html
<!DOCTYPE html>
<html lang="en">
<head>
<meta charset="utf-8">
<title>Brennan's Appliances – Business Cards</title>
<link rel="stylesheet" href="https://fonts.googleapis.com/css2?family=Arimo:wght@400;700&display=swap">
<style>
  :root {
    --backdrop: #7c4626;
    --kraft-light: #d2ac80;
    --kraft-mid: #c39a6c;
    --kraft-dark: #b38759;
    --ink: #111111;
  }
  * { box-sizing: border-box; margin: 0; padding: 0; }
  html, body { width: 1200px; height: 900px; overflow: hidden; }
  body {
    background: var(--backdrop);
    font-family: "Arimo", Arial, sans-serif;
    color: var(--ink);
    position: relative;
  }
  .card {
    position: absolute;
    width: 556px;
    height: 343px;
    overflow: hidden;
    background: radial-gradient(ellipse at 40% 30%, var(--kraft-light), var(--kraft-mid) 55%, var(--kraft-dark));
  }
  .card--front { left: 330px; top: 90px; }
  .card--back { left: 330px; top: 469px; }

  .employee { position: absolute; left: 32px; top: 48px; }
  .employee__name { font-size: 20px; font-weight: 700; letter-spacing: 0.3px; }
  .employee__title, .employee__branch { font-size: 15.5px; line-height: 21px; }
  .employee__title { margin-top: 5px; }

  .brand-name {
    position: absolute;
    font-weight: 700;
    color: var(--ink);
    text-transform: uppercase;
    line-height: 1.05;
    text-align: center;
  }
  .card--front .brand-name { left: 290px; top: 112px; width: 240px; font-size: 24px; }
  .card--back .brand-name { left: 120px; top: 120px; width: 320px; font-size: 32px; }

  .contacts { position: absolute; left: 32px; top: 183px; list-style: none; }
  .contacts li {
    display: flex; align-items: center; gap: 6px;
    font-size: 15.5px; height: 21px;
  }
  .contacts svg { width: 17px; height: 17px; flex: none; }

  .store {
    position: absolute;
    text-align: center;
    border-top: 1.5px solid var(--ink);
    padding-top: 6px;
    font-size: 15.5px;
    line-height: 21px;
    white-space: nowrap;
  }
  .store__phone { font-weight: 700; }
  .card--front .store { left: 40px; width: 475px; top: 280px; }
  .card--back .store { left: 134px; width: 290px; top: 281px; }
</style>
</head>
<body>

  <section class="card card--front" aria-label="Business card front">
    <div class="employee">
      <h1 class="employee__name">DANA WHITFIELD</h1>
      <p class="employee__title">Bargain Basement Supervisor</p>
      <p class="employee__branch">Lisbon</p>
    </div>

    <p class="brand-name">Brennan's Appliances</p>

    <ul class="contacts">
      <li>
        <svg viewBox="0 0 16 16" aria-hidden="true"><rect x="1" y="1" width="14" height="14" rx="2" fill="none" stroke="#111" stroke-width="1.5"/><path d="M5 4.2c.5-.3 1-.2 1.3.3l.6 1.2c.2.4 0 .8-.3 1l-.5.4c.4.9 1 1.6 1.9 2l.4-.5c.3-.3.7-.4 1-.2l1.2.6c.5.3.6.8.3 1.3-.6.9-1.6 1.2-2.6.7-2-1-3.4-2.4-4.1-4.3-.3-.9 0-1.9.8-2.5z" fill="#111"/></svg>
        <span>(860) 555-0142 ext. 10</span>
      </li>
      <li>
        <svg viewBox="0 0 16 16" aria-hidden="true"><rect x="1" y="3.5" width="14" height="9.5" fill="#111"/><path d="M1.5 4l6.5 5 6.5-5" fill="none" stroke="#c9a074" stroke-width="1.2"/></svg>
        <span>danaw@brennansappliances.example</span>
      </li>
      <li>
        <svg viewBox="0 0 16 16" aria-hidden="true"><circle cx="8" cy="8" r="6.8" fill="none" stroke="#111" stroke-width="1.5"/><ellipse cx="8" cy="8" rx="3" ry="6.8" fill="none" stroke="#111" stroke-width="1.2"/><path d="M1.2 8h13.6M2.2 4.6h11.6M2.2 11.4h11.6" stroke="#111" stroke-width="1.1"/></svg>
        <span>www.brennansappliances.example</span>
      </li>
    </ul>

    <div class="store">
      <p class="store__address">418 Harbor Mill Rd. Lisbon, CT 06351</p>
      <p class="store__phone">(860) 555-0142</p>
    </div>
  </section>

  <section class="card card--back" aria-label="Business card back">
    <p class="brand-name">Brennan's Appliances</p>
    <div class="store">
      <p class="store__address">57 Cedar Rd. Rivermouth, CT 06390</p>
      <p class="store__phone">(860) 555-0187</p>
    </div>
  </section>

</body>
</html>
```